Premium Personal Brand — Facebook Banner (Used Across All Platforms)

Update — Additional Color Direction
In addition to the dark charcoal/slate direction already described, I'm also interested in seeing variants with:
Dark navy blue — Deep, authoritative, intelligence-community feel. Same textured/matte treatment, not flat or bright.
Warm charcoal with steel blue accent — Keep the dark base but introduce a subtle steel blue gradient, accent line, or tonal shift. Sophisticated, modern, adds dimension without adding color noise.
Both should maintain the same premium, restrained, architectural feel described in the original brief. No bright blues, no corporate PowerPoint energy — think midnight, think depth, think weight.
Everything else in the brief remains the same.
I am building a premium personal brand as an executive advisor to founders ($5M+ revenue).
This contest is Facebook-banner–focused, but the design must represent a visual system that will be reused across:
- LinkedIn
- YouTube
I- nstagram
- X (Twitter)
- Website hero sections and other brand touchpoints
Think of the Facebook banner as the primary expression of the brand — not a one-off graphic.
This project is about discovering a high-end visual style and brand feel, not decoration.
What to design
Please submit one cohesive visual system, shown primarily as:
- Facebook banner (primary focus)
The same design language should clearly translate to all platforms listed above.
Designers are responsible for using the current recommended dimensions for each platform.
Quick clarification on background direction:
Backgrounds should have depth and texture, not flat color fields. Avoid pure white, light grey, or solid black backgrounds. Think matte, architectural materials — stone, graphite, concrete, steel — not blank canvases. Subtle tonal variation is encouraged. Obvious gradients or decorative patterns are not.
Text to use
Primary Headline:
- Your Business Is Too Valuable To Be Run On Hope.
Subheadline:
- You didn’t build a business to become its prisoner.
Name:
Paul Whitaker
The headline should be the dominant visual element.
Logo note (important)
My personal logo is currently being finalized.
For this contest:
- Use a simple “PW” monogram placeholder
- Clean, bold, geometric sans-serif
- Do not design a logo
- The winning design must allow an easy logo swap later.
Headshot note (important)
- Please do not include a headshot in the banner design.
- Most platforms display a circular profile image separately.
- The banner should stand on its own using typography, layout, and tone only.
- Design the banner assuming the profile photo will sit nearby, not inside the banner.
Style direction
The design should feel:
- Premium
- Calm
- Confident
- Restrained
- High-trust
- Dark, neutral backgrounds are preferred.
- Fewer elements are better than more.
Think:
- Owner-level advisor
- Private equity / boardroom tone
- Industrial, Modern, Minimalist, Elite, Architectural, not decorative
What to avoid
Please do not submit designs that feel:
- Promotional, hype-driven, or salesy
- Like a coach, guru, or agency
- Bright, colorful, or gradient-heavy
- Busy or over-designed
- Based on stock photos
- No motivational speaker energy.
Reaction test
- If someone sees this banner on Facebook (or later on LinkedIn, YouTube, etc.), the reaction should be:
“That person is serious. I’d trust them with important decisions.”
Final note
- I am not looking for many variations.
- I am looking for one strong visual direction you believe in.
Simple beats clever.
- Restraint beats decoration.

```html
<!DOCTYPE html>
<html lang="en">
<head>
<meta charset="utf-8">
<title>Paul Whitaker — Banner System</title>
<link rel="stylesheet" href="https://fonts.googleapis.com/css2?family=Poppins:wght@400;600;700&display=swap">
<style>
  :root {
    --sheet: #ffffff;
    --ink: #111111;
    --night: #0f0c1e;
    --night-deep: #08071a;
    --violet-glow: #2a2150;
    --violet-mid: #1b1538;
    --text-light: #ffffff;
    --rule: rgba(160, 150, 210, 0.22);
  }
  * { margin: 0; padding: 0; box-sizing: border-box; }
  html, body {
    width: 1200px;
    height: 1200px;
    overflow: hidden;
    background: var(--sheet);
  }
  .sheet {
    position: relative;
    width: 1200px;
    height: 1200px;
    font-family: "Poppins", sans-serif;
  }
  .variant-label {
    position: absolute;
    left: 43px;
    font-weight: 700;
    font-size: 32px;
    line-height: 1;
    color: var(--ink);
  }
  .banner {
    position: absolute;
    overflow: hidden;
    color: var(--text-light);
    text-align: center;
  }
  .banner__texture {
    position: absolute;
    inset: 0;
    background:
      radial-gradient(ellipse 70% 90% at 80% 35%, var(--violet-glow) 0%, transparent 60%),
      radial-gradient(ellipse 60% 80% at 12% 20%, var(--violet-mid) 0%, transparent 65%),
      radial-gradient(circle at 50% 120%, rgba(60, 48, 110, 0.35) 0%, transparent 55%),
      linear-gradient(160deg, var(--night) 0%, var(--night-deep) 55%, var(--night) 100%);
  }
  .banner > .line {
    position: absolute;
    left: 0;
    right: 0;
    transform: translateY(-50%);
    white-space: nowrap;
  }
  .headline {
    font-weight: 700;
    font-size: 34px;
    line-height: 1;
    letter-spacing: 0.2px;
  }
  .subheadline {
    font-weight: 400;
    font-size: 19.5px;
    line-height: 1;
  }
  .monogram {
    font-weight: 700;
    font-size: 52px;
    line-height: 1;
    letter-spacing: -1px;
  }
  .name {
    font-weight: 600;
    font-size: 25px;
    line-height: 1;
  }
  .rule {
    position: absolute;
    left: 12%;
    right: 12%;
    height: 1px;
    background: linear-gradient(90deg, transparent, var(--rule) 20%, var(--rule) 80%, transparent);
  }

  .banner--overall { left: 43px; top: 76px; width: 756px; height: 320px; }
  .banner--desktop { left: 43px; top: 472px; width: 756px; height: 280px; }
  .banner--mobile  { left: 45px; top: 830px; width: 569px; height: 320px; }
</style>
</head>
<body>
<main class="sheet">

  <h2 class="variant-label" style="top:27px;">Overall design</h2>
  <section class="banner banner--overall">
    <div class="banner__texture" role="img" aria-label="Dark navy architectural background with curved concentric structure"></div>
    <p class="line headline" style="top:54px;">Your Business Is Too Valuable</p>
    <p class="line headline" style="top:97px;">To Be Run On Hope.</p>
    <span class="rule" style="top:128px;"></span>
    <p class="line subheadline" style="top:148px;">You didn’t build a business to become its prisoner.</p>
    <span class="rule" style="top:179px;"></span>
    <p class="line monogram" style="top:208px;">PW</p>
    <p class="line name" style="top:262px;">Paul Whitaker</p>
  </section>

  <h2 class="variant-label" style="top:423px;">Desktop</h2>
  <section class="banner banner--desktop">
    <div class="banner__texture" role="img" aria-label="Dark navy architectural background with curved concentric structure"></div>
    <p class="line headline" style="top:34px;">Your Business Is Too Valuable</p>
    <p class="line headline" style="top:76px;">To Be Run On Hope.</p>
    <span class="rule" style="top:108px;"></span>
    <p class="line subheadline" style="top:128px;">You didn’t build a business to become its prisoner.</p>
    <span class="rule" style="top:158px;"></span>
    <p class="line monogram" style="top:188px;">PW</p>
    <p class="line name" style="top:242px;">Paul Whitaker</p>
  </section>

  <h2 class="variant-label" style="top:779px;">Mobile</h2>
  <section class="banner banner--mobile">
    <div class="banner__texture" role="img" aria-label="Dark navy architectural background with curved concentric structure"></div>
    <p class="line headline" style="top:54px;">Your Business Is Too Valuable</p>
    <p class="line headline" style="top:97px;">To Be Run On Hope.</p>
    <span class="rule" style="top:128px;"></span>
    <p class="line subheadline" style="top:148px;">You didn’t build a business to become its prisoner.</p>
    <span class="rule" style="top:179px;"></span>
    <p class="line monogram" style="top:208px;">PW</p>
    <p class="line name" style="top:262px;">Paul Whitaker</p>
  </section>

</main>
</body>
</html>
```